Briefpapier klangrabatt17
Die Zusammenarbeit war vorbildlich. Sehr schnelle Reaktion auf unsere Wünsche und eine sehr gute Umsetzung des Projektes. Danke, wir werden wieder auf Sie zurückkommen für unseren nächsten Flyer.
Zielgruppe
Wir verkaufen Musiknoten, Lehr-DVDs für Instrumente aus Klassik, Rock, Pop, Jazz etc.
Da wir in letzter Zeit mehr Musiknoten aus der Klassik haben, wäre es sinnvoll, den Briefbogen seriös zu gestalten.
Aufgabenstellung
Wir bitten um Gestaltung eines Briefbogens mit den folgenden Informationen:
Anschrift: klangrabatt17
www.klangrabatt17.example
Wir haben folgende Homepage:
http://laden.tonfinder.example/38527/Home.html
Der Zusatz lyra digital sollte allerdings nicht im Brieflogo erscheinen.
Also Logo nur mit "klangrabatt17" und dem Zusatz: Ihr Spezialist für Musiknoten und Lehr-DVD's
Bitte die in der angefügten Datei verwandten Farben verwenden (gelb und rot)

```html
<!DOCTYPE html>
<html lang="de">
<head>
<meta charset="utf-8">
<title>Briefpapier klangrabatt17</title>
<link rel="stylesheet" href="https://fonts.googleapis.com/css2?family=Arimo&family=Open+Sans:wght@400;700&family=PT+Sans&family=Questrial&display=swap">
<style>
  :root {
    --backdrop: #3b4a55;
    --paper: #ffffff;
    --brand-red: #e30613;
    --brand-yellow: #f39200;
    --logo-yellow: #f7a823;
    --text-grey: #8a8a8a;
    --text-dark: #3c3c3c;
    --text-mid: #6b6b6b;
    --ink-blue: #2b6cc4;
    --watermark: #f4f4f4;
  }
  * { margin: 0; padding: 0; box-sizing: border-box; }
  html, body {
    width: 943px; height: 1200px; overflow: hidden;
    background: var(--backdrop);
  }
  .letterhead {
    position: absolute; left: 45px; top: 0;
    width: 853px; height: 1200px;
    background: var(--paper);
    font-family: "Questrial", "Century Gothic", sans-serif;
    color: var(--text-grey);
    overflow: hidden;
  }
  .side-bar {
    position: absolute; left: 0; top: 0;
    width: 35px; height: 1028px;
    background: var(--brand-red);
  }
  .side-square {
    position: absolute; left: 0; width: 35px; height: 32px;
    background: var(--brand-yellow);
  }
  .abs { position: absolute; white-space: nowrap; }

  .corner-mark {
    position: absolute; left: 500px; top: 960px;
    width: 240px; height: 240px; border-radius: 50%;
    background: var(--watermark);
  }

  .sender-line { left: 92px; top: 156px; font-size: 11px; line-height: 14px; }
  .sender-line .name { color: var(--brand-red); font-weight: 700; font-family: "Open Sans", sans-serif; }

  .brand-name {
    left: 434px; top: 92px;
    font-family: "Open Sans", sans-serif; font-weight: 700;
    font-size: 46px; line-height: 60px; color: var(--brand-red);
    letter-spacing: -0.5px;
  }
  .brand-accent {
    position: absolute; left: 772px; top: 104px;
    width: 40px; height: 40px; background: var(--logo-yellow);
  }
  .brand-tagline { left: 434px; top: 160px; font-size: 16.5px; color: var(--text-grey); }

  .contact { font-size: 13.5px; color: var(--text-grey); display: flex; align-items: center; gap: 8px; }
  .contact svg { width: 13px; height: 13px; fill: var(--text-mid); }

  .meta { font-size: 13px; color: var(--text-grey); }
  .date { right: 101px; font-size: 13px; }

  .recipient {
    left: 92px; top: 368px;
    font-family: "Arimo", Arial, sans-serif; font-size: 14.5px; line-height: 19.5px;
    color: var(--text-mid);
  }
  .recipient p.gap { margin-top: 19.5px; }

  .body-copy {
    position: absolute; left: 92px; top: 566px; width: 668px;
    font-family: "PT Sans", Arial, sans-serif; font-size: 15.3px; line-height: 20px;
    color: var(--text-dark);
  }
  .body-copy p + p { margin-top: 4px; }

  .closing { left: 511px; top: 872px; font-family: "Arimo", Arial, sans-serif; font-size: 16.5px; color: var(--text-mid); }
  .signature-area { position: absolute; left: 505px; top: 898px; width: 130px; height: 80px; }

  .footer-label { left: 61px; font-size: 14px; color: var(--brand-red); }
  .footer-detail { left: 61px; font-size: 10.5px; color: var(--text-grey); }
  .footer-detail b { font-weight: 400; color: var(--text-mid); }
  .footer-detail .sep { color: var(--brand-red); padding: 0 4px; }
</style>
</head>
<body>
<main class="letterhead">
  <div class="corner-mark" aria-hidden="true"></div>
  <div class="side-bar"></div>
  <div class="side-square" style="top:1037px"></div>
  <div class="side-square" style="top:1076px"></div>
  <div class="side-square" style="top:1114px"></div>

  <div class="abs sender-line"><span class="name">klangrabatt17</span>- Inh. Lorenz Auerbach<br>Birkenweg 8 - 54321 Tannfeld</div>

  <div class="abs brand-name">klangrabatt17</div>
  <div class="brand-accent" aria-hidden="true"></div>
  <div class="abs brand-tagline">Ihr Spezialist für Musiknoten und Lehr-DVD's</div>

  <div class="abs contact" style="left:434px; top:190px">
    <svg viewBox="0 0 16 16"><path d="M8 1a6 6 0 0 0-6 6v4a2 2 0 0 0 2 2h1V8H3.5V7a4.5 4.5 0 0 1 9 0v1H11v5h1a2 2 0 0 0 2-2V7a6 6 0 0 0-6-6z"/></svg>
    <span>+49 5550 1234</span>
  </div>
  <div class="abs contact" style="left:434px; top:209px">
    <svg viewBox="0 0 16 16"><path d="M4 1h8v4H4zM2 6h12a1 1 0 0 1 1 1v5h-3v3H4v-3H1V7a1 1 0 0 1 1-1zm3 5v3h6v-3z"/></svg>
    <span>+49 5550 1239</span>
  </div>
  <div class="abs contact" style="left:565px; top:190px">
    <svg viewBox="0 0 16 16"><path d="M1 3h14v10H1zm1.5 1.5v.3L8 9l5.5-4.2v-.3zM2.5 6.6v4.9h11V6.6L8 10.8z"/></svg>
    <span>info@klangrabatt17.example</span>
  </div>
  <div class="abs contact" style="left:565px; top:209px">
    <svg viewBox="0 0 16 16"><path d="M8 1a7 7 0 1 0 0 14A7 7 0 0 0 8 1zm0 1.5c.8 0 1.8 1.7 2.1 4.5H5.9C6.2 4.2 7.2 2.5 8 2.5zM2.6 7h1.9c0-1.3.3-2.6.8-3.5A5.5 5.5 0 0 0 2.6 7zm8.9 0h1.9a5.5 5.5 0 0 0-2.7-3.5c.5.9.8 2.2.8 3.5zM2.6 9a5.5 5.5 0 0 0 2.7 3.5c-.5-.9-.8-2.2-.8-3.5zm3.3 0c.3 2.8 1.3 4.5 2.1 4.5s1.8-1.7 2.1-4.5zm5.6 0c0 1.3-.3 2.6-.8 3.5A5.5 5.5 0 0 0 13.4 9z"/></svg>
    <span>www.klangrabatt17.example</span>
  </div>

  <div class="abs meta" style="left:92px; top:300px">Carl Brenner</div>
  <div class="abs meta" style="left:92px; top:320px">Re: ( To what this letter refers )</div>
  <div class="abs date" style="top:300px">London September 27, 2045</div>

  <div class="abs recipient">
    <p>Recipient's Name</p>
    <p>Company Name</p>
    <p>Adress</p>
    <p class="gap">Atention (Recipien's Name)</p>
    <p class="gap">Dear (Recipient's Name)</p>
    <p class="gap">( Subject )</p>
  </div>

  <section class="body-copy">
    <p>Lorem ipsum dolor sit amet, consectetur adipiscing elit. Nam urna dui, accumsan auctor gravida nec, tempus nec ante&nbsp; Nam vitae mi et est feugiat interdum&nbsp; Nam eget tortor ligula&nbsp; consectetur tristique risus. Vivamus quis libero vel odio dictum rhoncus. Donec non metus sed quam posuere vestibulum. Quisque feugiat, mi quis congue egestas, lectus dui rutrum odio, et dignissim justo lorem quis nunc. Duis euismod purus sit amet orci cursus congue&nbsp; Nulla vitae fermentum ante&nbsp; Integer interdum massa vitae nisi scelerisque eu vulputate leo malesuada. Nulla in purus eu augue aliquet tempor nec condimentum neque. Nullam sed nulla metus.</p>
    <p>Suspendisse a risus quis risus condimentum gravida a in lacus&nbsp; Aenean vel ipsum venenatis velit lobortis ultricies a nec risus. In hac habitasse platea dictumst. Aenean gravida rutrum accumsan. Nulla accumsan ullamcorper mauris ac iaculis&nbsp; Donec volutpat&nbsp; turpis ac porta tincidunt&nbsp; felis neque blandit augue&nbsp; eget pharetra tortor turpis quis metus&nbsp; Etiam non risus ac est luctus ornare&nbsp; Vivamus porta, velit quis pharetra pellentesque, urna nisi tempus quam, non eleifend nulla leo vel dui.</p>
  </section>

  <div class="abs closing">Best Regards</div>
  <svg class="signature-area" viewBox="0 0 130 80">
    <rect x="0" y="6" width="88" height="26" rx="4" fill="var(--ink-blue)" opacity="0.18" role="img" aria-label="Handschriftliche Unterschrift"/>
    <circle cx="82" cy="38" r="32" fill="none" stroke="#6d7fb0" stroke-width="1.5" opacity="0.5"/>
  </svg>

  <div class="abs footer-label" style="top:1040px">Anschrift</div>
  <div class="abs footer-detail" style="top:1057px"><b>klangrabatt17</b> - Inh. Lorenz Auerbach-Birkenweg 8 - 54321 Tannfeld</div>

  <div class="abs footer-label" style="top:1078px">Unternehmen</div>
  <div class="abs footer-detail" style="top:1095px"><b>Geschäftsführer:</b> Lorenz Auerbach<span class="sep">|</span><b>Steuernummer:</b> 201/447/30518<span class="sep">|</span><b>UST-ID-Nr.</b> DE 000123456</div>

  <div class="abs footer-label" style="top:1116px">Bankverbindung</div>
  <div class="abs footer-detail" style="top:1134px">Stadtbank Tannfeld<span class="sep">|</span><b>IBAN:</b> DE00 1234 5678 9012 3456 78<span class="sep">|</span><b>BIC:</b> TANNDEX1XXX</div>
</main>
</body>
</html>
```